Coffee Fundraising Label for a coffee bag

We would like an update to a label for our coffee fundraising bags. We currently fundraise to all types of groups, schools, sports teams, etc... These are the labels that go out on our coffee fundraising bags. All the details are included in the label Design document attached. They need to be simple to read but playful as they are for fundraisers.

Target Market(s)

Anyone who fundraises. Sports teams, schools, bands, non-profits and many more...

Requirements
Must have
• the brief tells you what the must haves are..
• Must have the larkspur roast drives logo. If you see the sticker file perhaps placing the logo in one of those colors might look good. If you look at the colors on the sticker file, these at the colors we using on our new web site... would like the background color of the label to stay black, unless you can convince us otherwise
Nice to have
• see the brief...
Should not have
• See the brief....

```html
<!DOCTYPE html>
<html lang="en">
<head>
<meta charset="utf-8">
<title>Larkspur Roast Drives – Bag Label</title>
<link href="https://fonts.googleapis.com/css2?family=Oswald:wght@500;600&display=swap" rel="stylesheet">
<style>
  :root {
    --page: #e9e7e4;
    --label-black: #262626;
    --pattern-tone: #2f2f2f;
    --brand-orange: #e8542a;
    --brand-yellow: #f6a91c;
    --brand-green: #1f6b3a;
    --ink-dark: #231f1c;
    --banner-white: #f2f2f2;
  }
  html, body {
    margin: 0;
    width: 1061px;
    height: 1200px;
    overflow: hidden;
    background: var(--page);
    font-family: "Oswald", "Arial Narrow", sans-serif;
  }
  .label {
    position: absolute;
    left: 180px;
    top: 50px;
    width: 700px;
    height: 1100px;
    background: var(--label-black);
    overflow: hidden;
  }
  .label-texture {
    position: absolute;
    inset: 0;
    background: linear-gradient(180deg, var(--pattern-tone), var(--label-black));
  }
  .brand-band {
    position: absolute;
    left: 150px;
    top: 0;
    width: 410px;
    height: 560px;
    background: var(--brand-orange);
  }
  .brand-seal {
    position: absolute;
    left: 130px;
    top: 75px;
    width: 450px;
    height: 450px;
    border-radius: 50%;
    background: var(--brand-yellow);
    display: flex;
    align-items: center;
    justify-content: center;
  }
  .brand-name {
    color: var(--ink-dark);
    font-weight: 600;
    font-size: 58px;
    line-height: 1.05;
    text-align: center;
    text-transform: uppercase;
    letter-spacing: 2px;
  }
  .thanks-ribbon {
    position: absolute;
    left: 40px;
    top: 470px;
    width: 620px;
    height: 110px;
  }
  .thanks-text {
    position: absolute;
    left: 40px;
    top: 487px;
    width: 620px;
    text-align: center;
    color: var(--brand-yellow);
    font-weight: 500;
    font-size: 40px;
    transform: rotate(-4deg);
  }
  .tagline {
    position: absolute;
    top: 612px;
    width: 100%;
    text-align: center;
    color: var(--brand-orange);
    font-weight: 500;
    font-size: 34px;
    letter-spacing: 1px;
  }
  .fill-banner {
    position: absolute;
    left: 40px;
    top: 680px;
    width: 620px;
    height: 230px;
  }
  .roaster-info {
    position: absolute;
    top: 950px;
    width: 100%;
    text-align: center;
    color: var(--brand-yellow);
    font-weight: 500;
    font-size: 30px;
    line-height: 1.4;
  }
  .roaster-info p { margin: 0; }
</style>
</head>
<body>
  <div class="label">
    <div class="label-texture" role="img" aria-label="Dark charcoal diamond pattern background"></div>
    <div class="brand-band"></div>
    <div class="brand-seal">
      <div class="brand-name">Larkspur<br>Roast<br>Drives</div>
    </div>

    <svg class="thanks-ribbon" viewBox="0 0 620 110" aria-hidden="true">
      <polygon points="0,50 70,40 80,100 20,105" fill="var(--brand-green)"/>
      <polygon points="620,20 550,20 545,80 600,70" fill="var(--brand-green)"/>
      <polygon points="55,45 85,95 95,55" fill="var(--brand-orange)"/>
      <polygon points="565,20 540,75 530,35" fill="var(--brand-orange)"/>
      <polygon points="60,30 570,0 575,55 70,95" fill="var(--brand-green)"/>
    </svg>
    <div class="thanks-text">Thank you for your support!</div>

    <div class="tagline">ETHICALLY SOURCED COFFEE</div>

    <svg class="fill-banner" viewBox="0 0 620 230" aria-hidden="true">
      <path d="M0,20 Q160,0 310,15 T620,0 L605,110 L620,200 Q460,215 310,210 T0,230 L15,120 Z" fill="var(--banner-white)"/>
    </svg>

    <div class="roaster-info">
      <p>Custom Roasted in Fernhollow, BC</p>
      <p>www.larkspurroastdrives.ca</p>
    </div>
  </div>
</body>
</html>
```